依頼詳細
引越を考えているお客様にチラシを渡して頂くため、不動産店舗を回って交渉をしています。
その際に営業の皆様に渡す名刺です。
「引越業者選び面倒臭い!とお思いの皆様へ。」
「数多くある引越業者から安くしっかりした業者を選定してくれる」「面倒なことを全て引き受けてくれる」ことが売りの会社です。

チラシはお客様向けなのでポップな雰囲気で分かり易く作って頂いていますが、名刺のデザインとしては
信頼感や堅実さを押し出すのが良いのかなと思っています。

添付のファイルは会社のロゴです。

それでは宜しくお願いいたします。
記載項目
株式会社brightway/役職名/佐藤 健一/KENICHI SATO/本社所在地 〒105-0021 東京都港区東新橋4-2-8/代表 03-5417-3861/お見積専用ダイヤル0120-583-216/HP www.bwaymv.co.jp/Mail info.bwaymv.co.jp/
希望イメージ
シンプル 複雑
単色 カラフル
暗い 明るい
日常 高級
遊び心 厳粛
未来的 伝統的
女性的 男性的
希望する色
納品ファイル
• 高解像度JPG (.jpg)
• イラストレーター形式 (.ai)
補足説明
添付しましたイラストレーターファイル(会社ロゴ)につきまして、バージョンが新しいために開けない、古く出来ないかとのご相談がありました。
取り急ぎ、解像度が粗いですがjpgファイルを添付しますので、仮でこれをお使い下さい。

どれを使ってあっても、全体のデザインが気に入れば採用します。
■ 選んだ理由

お伝えしたかった意図をよく汲んで頂いたこと、見た目の爽やかさと分かりやすさが決め手となりました。
こちらからの要望も気持ち良く受けて頂き、感謝しています。

■ 提案者全員のお礼・コメント

とても素晴らしいご提案を沢山頂きました。
惜しくも選外とさせて頂いた方も、また別の機会にお付き合い頂ければ幸いです。

```html
<!DOCTYPE html>
<html lang="ja">
<head>
<meta charset="utf-8">
<title>株式会社brightway 名刺</title>
<link href="https://fonts.googleapis.com/css2?family=Noto+Sans+JP:wght@400;500;700&display=swap" rel="stylesheet">
<style>
  :root {
    --paper: #ffffff;
    --page: #ffffff;
    --ink: #3a3a3a;
    --ink-soft: #555555;
    --label-line: #8a8a8a;
    --accent: #7cb342;
    --caption: #333333;
  }
  * { margin: 0; padding: 0; box-sizing: border-box; }
  html, body {
    width: 897px; height: 1200px; overflow: hidden;
    background: var(--page);
    font-family: "Noto Sans JP", sans-serif;
    color: var(--ink);
  }
  .sheet { position: relative; width: 897px; height: 1200px; }
  .side-caption {
    position: absolute; left: 14px;
    font-size: 22px; color: var(--caption); font-weight: 400;
  }
  .side-caption.front { top: 2px; }
  .side-caption.back { top: 602px; }
  .card {
    position: absolute; left: 45px; width: 807px; overflow: hidden;
    background: var(--paper);
    box-shadow: 6px 8px 14px rgba(0,0,0,0.35);
  }
  .card.front { top: 36px; height: 547px; }
  .card.back { top: 652px; height: 528px; }

  .title-bar {
    position: absolute; left: 21px; top: 110px;
    width: 13px; height: 130px; background: var(--accent);
  }
  .role { position: absolute; left: 46px; top: 110px; font-size: 16px; line-height: 1.3; }
  .person-name {
    position: absolute; left: 46px; top: 134px;
    font-size: 32px; font-weight: 700; letter-spacing: 7px; line-height: 1.3;
  }
  .person-roman { position: absolute; left: 46px; top: 204px; font-size: 15px; line-height: 1.3; }
  .company {
    position: absolute; left: 46px; top: 258px;
    font-size: 21px; font-weight: 700; line-height: 1.3;
  }
  .contact-list { position: absolute; left: 46px; top: 300px; list-style: none; }
  .contact-list li {
    display: flex; align-items: center; height: 37px;
  }
  .contact-label {
    width: 146px; height: 28px; border: 2px solid var(--label-line);
    border-radius: 8px; font-size: 15px; color: var(--ink-soft);
    display: flex; align-items: center; justify-content: center;
    letter-spacing: 6px;
  }
  .contact-value {
    margin-left: 18px; font-size: 23px; color: var(--ink-soft); letter-spacing: 1px; line-height: 1;
  }
  .contact-value.address { font-size: 15px; letter-spacing: 0; }

  .brand-name {
    position: absolute; font-weight: 700; color: var(--accent);
    letter-spacing: 1px; line-height: 1; text-align: center; white-space: nowrap;
  }
  .card.front .brand-name { left: 480px; width: 290px; top: 248px; font-size: 50px; }
  .card.back .brand-name { left: 0; right: 0; top: 280px; font-size: 60px; }
</style>
</head>
<body>
<div class="sheet">
  <p class="side-caption front">Front</p>
  <section class="card front">
    <div class="title-bar"></div>
    <p class="role">代表取締役</p>
    <h1 class="person-name">佐藤 健一</h1>
    <p class="person-roman">KENICHI SATO</p>
    <p class="company">株式会社 brightway</p>
    <ul class="contact-list">
      <li><span class="contact-label">所在地</span><span class="contact-value address">〒105-0021 東京都港区東新橋4-2-8</span></li>
      <li><span class="contact-label">代表電話</span><span class="contact-value">03-5417-3861</span></li>
      <li><span class="contact-label">見積専用</span><span class="contact-value">0120-583-216</span></li>
      <li><span class="contact-label">URL</span><span class="contact-value">www.bwaymv.co.jp</span></li>
      <li><span class="contact-label">E-mail</span><span class="contact-value">info.bwaymv.co.jp</span></li>
    </ul>
    <p class="brand-name">brightway</p>
  </section>

  <p class="side-caption back">Back</p>
  <section class="card back">
    <p class="brand-name">brightway</p>
  </section>
</div>
</body>
</html>
```